Elegant Black Candle Label Design!

I need a 2.375" tall by 3.0" wide candle label design. I'm looking for simple and elegant. Black label with silver leaf border and lettering. Label needs to have the following information on it: Fern Hollow Candle Co. as the company name, scent name in the middle and in smaller font, it needs to say Made in USA, All Natural, 8oz. Attached photos are for inspiration.

Target Market(s)

People looking for high end, all natural candle fragrances

Industry/Entity Type

Candle-Spa

Colors

Designer to choose only greyscale colors for use in the design.

Requirements
Must have
• Company Name, Scent (ability to change scent names), All Natural, Made in USA, 8oz
Nice to have
• Black background, silver leaf border and silver leaf font. Elegant fonts maybe slightly cursive

```html
<!DOCTYPE html>
<html lang="en">
<head>
<meta charset="UTF-8">
<title>Fern Hollow Candle Co. – Candle Label</title>
<link rel="stylesheet" href="https://fonts.googleapis.com/css2?family=Merriweather:wght@300;400&display=swap">
<style>
  :root {
    --backdrop: #e4e4e4;
    --label-black: #222223;
    --silver-line: #a6a6a6;
    --silver-text: #d9d9d9;
    --silver-soft: #c4c4c4;
  }
  html, body {
    margin: 0;
    padding: 0;
    width: 1200px;
    height: 848px;
    overflow: hidden;
    background: var(--backdrop);
  }
  .canvas {
    position: relative;
    width: 1200px;
    height: 848px;
  }
  .candle-label {
    position: absolute;
    left: 220px;
    top: 124px;
    width: 760px;
    height: 600px;
    background: var(--label-black);
    box-shadow: 0 2px 6px rgba(0, 0, 0, 0.18);
    font-family: "Merriweather", Georgia, serif;
  }
  .label-frames {
    position: absolute;
    inset: 0;
  }
  .frame-line {
    fill: none;
    stroke: var(--silver-line);
    stroke-width: 1.3;
  }
  .logo-plate {
    fill: var(--label-black);
  }
  .brand-block {
    position: absolute;
    left: 189px;
    top: 103px;
    width: 379px;
    height: 163px;
    display: flex;
    flex-direction: column;
    align-items: center;
    justify-content: center;
    color: var(--silver-text);
    font-weight: 300;
  }
  .brand-name {
    font-size: 36px;
    line-height: 1.1;
    letter-spacing: 1px;
  }
  .brand-suffix {
    margin-top: 8px;
    font-size: 14px;
    letter-spacing: 6px;
    padding-left: 6px;
  }
  .scent-name {
    position: absolute;
    left: 0;
    right: 0;
    top: 330px;
    text-align: center;
    font-size: 34px;
    font-weight: 400;
    color: var(--silver-text);
    letter-spacing: 0.5px;
  }
  .product-details {
    position: absolute;
    left: 0;
    right: 0;
    top: 432px;
    display: flex;
    justify-content: center;
    gap: 22px;
    font-size: 24px;
    font-weight: 300;
    color: var(--silver-soft);
  }
</style>
</head>
<body>
  <main class="canvas">
    <section class="candle-label">
      <svg class="label-frames" width="760" height="600" viewBox="0 0 760 600" aria-hidden="true">
        <rect class="frame-line" x="48" y="180" width="662" height="370"/>
        <rect class="frame-line" x="54" y="186" width="650" height="358"/>
        <rect class="logo-plate" x="189" y="103" width="379" height="163"/>
        <rect class="frame-line" x="189" y="103" width="379" height="163"/>
        <rect class="frame-line" x="195" y="109" width="367" height="151"/>
      </svg>

      <div class="brand-block">
        <span class="brand-name">Fern Hollow</span>
        <span class="brand-suffix">CANDLE CO.</span>
      </div>

      <h1 class="scent-name" style="margin:0">SCENT NAME</h1>

      <p class="product-details" style="margin:0">
        <span class="detail">All Natural</span>
        <span class="detail">8oz</span>
        <span class="detail">Made in USA</span>
      </p>
    </section>
  </main>
</body>
</html>
```